I am looking for a modern style design for a podcast cover art.
Titled: Open Harbor with R.K. Thistlewood
colors to stay in the grays, reds, blacks, white, gold, and maybe blues if it fits well. I attached a mock up of what we are going for and a current podcast cover we drew inspiration from.
Colors
3276b5
ec1f27
f04a50
1b1b1b
474747
919191
d2d2d2

```html
<!DOCTYPE html>
<html lang="en">
<head>
<meta charset="utf-8">
<title>Open Harbor with R.K. Thistlewood</title>
<link rel="stylesheet" href="https://fonts.googleapis.com/css2?family=Anton&family=Saira:wght@600&display=swap">
<style>
  :root {
    --wall-light: #f3f2ef;
    --wall-mid: #dcdad5;
    --panel-blue: #17599e;
    --accent-blue: #1371b8;
    --white: #ffffff;
    --ink: #111111;
    --title-magenta: #d80d55;
    --photo-light: #9a9a9a;
    --photo-dark: #262626;
  }
  html, body {
    margin: 0;
    padding: 0;
    overflow: hidden;
    background: var(--white);
  }
  .cover {
    position: relative;
    width: 1200px;
    height: 849px;
    overflow: hidden;
  }
  .cover__wall {
    position: absolute;
    inset: 0;
    background: radial-gradient(ellipse at 50% 45%, var(--wall-light) 0%, var(--wall-mid) 100%);
  }
  .cover__panel {
    position: absolute;
    left: 277px;
    top: 62px;
    width: 768px;
    height: 543px;
    background: var(--panel-blue);
  }
  .cover__host-photo {
    position: absolute;
    left: 640px;
    top: 140px;
    width: 375px;
    height: 465px;
    border-radius: 120px 120px 0 0;
    background: linear-gradient(180deg, var(--photo-light) 0%, var(--photo-dark) 70%);
  }
  .cover__bar {
    position: absolute;
    height: 45px;
  }
  .cover__bar--blue {
    left: 958px;
    top: 128px;
    width: 175px;
    background: var(--accent-blue);
  }
  .cover__bar--white {
    left: 928px;
    top: 183px;
    width: 175px;
    background: var(--white);
  }
  .cover__type {
    position: absolute;
    inset: 0;
  }
  .host-line {
    font-family: "Anton", "Oswald", sans-serif;
    fill: var(--ink);
    text-transform: uppercase;
  }
  .show-title {
    font-family: "Saira", "Exo 2", sans-serif;
    font-weight: 600;
    fill: var(--title-magenta);
    text-transform: uppercase;
  }
</style>
</head>
<body>
  <main class="cover">
    <div class="cover__wall" role="img" aria-label="Whitewashed brick wall background"></div>
    <div class="cover__panel"></div>
    <div class="cover__host-photo" role="img" aria-label="Black and white photo of the host in a tuxedo and bow tie, pointing to the left"></div>
    <div class="cover__bar cover__bar--blue"></div>
    <div class="cover__bar cover__bar--white"></div>

    <svg class="cover__type" width="1200" height="849" viewBox="0 0 1200 849">
      <text class="host-line host-line--with" transform="translate(140 600) rotate(-90)"
            font-size="72" textLength="135" lengthAdjust="spacingAndGlyphs">With</text>
      <text class="host-line host-line--name" transform="translate(255 605) rotate(-90)"
            font-size="100" textLength="543" lengthAdjust="spacingAndGlyphs">R.K. Thistlewood</text>
      <text class="show-title" x="45" y="790" font-size="200"
            textLength="1115" lengthAdjust="spacingAndGlyphs">OpenHarbor</text>
    </svg>
  </main>
</body>
</html>
```